Gestalten Sie ein tolles Selbstliebe-Buchcover
Hallo,
schön, dass Sie sich für diese Ausschreibung interessieren. Wir suchen ein Cover für unser Buch, das wir im Selbstverlag veröffentlichen werden.
Titel: Ein Garten aus Mondlicht
Untertitel 1: Wie du dich von negativen Gedanken befreist und eine liebevolle Beziehung zu dir selbst aufbaust
Untertitel Teil 2: 12 lebensverändernde Monate voller positiver Impulse und Liebe für dich
Das Buch soll (mehrheitlich) Frauen unterstützen, eine liebevolle Beziehung zu sich selbst aufzubauen, negative Gedanken loszulassen und innere Ruhe zu finden.
Aufgabenstellung
Wir sind für jegliche Vorschläge im Rahmen des Themas, der Samples und der Schieberegler offen.
Wichtig ist allerdings
- dass das Design selbst in der kleinen Ansicht (Suchergebnisse) auf Kuvarto klar hervorsticht, das heißt dort klar erkennbar und die Schrift sofort lesbar ist. Es muss in klein „wirken“, weil viele mit dem Handy auf Kuvarto shoppen und die Ansicht in den Suchergebnissen dort noch kleiner ist.
- dass das Design die gezielt Emotionen vermittelt
Optimal wäre es, wenn Ihr keine Mockups hochladet. Das macht es viel schwieriger, die Designs einzuschätzen und miteinander zu vergleichen.

```html
<!DOCTYPE html>
<html lang="de">
<head>
<meta charset="utf-8">
<title>Ein Garten aus Mondlicht – Buchcover</title>
<link rel="stylesheet" href="https://fonts.googleapis.com/css2?family=Dancing+Script:wght@700&family=Fira+Sans:ital,wght@0,700;1,300;1,700&family=Montserrat:wght@500&display=swap">
<style>
  :root {
    --ink: #3b2a2e;
    --mint-light: #e4f7f1;
    --mint: #b9ede0;
    --mint-deep: #93e0cc;
    --line-art: #cdeee4;
  }
  * { margin: 0; padding: 0; box-sizing: border-box; }
  html, body { width: 798px; height: 1200px; overflow: hidden; }
  body { background: #ffffff; }
  .cover {
    position: relative;
    width: 798px;
    height: 1200px;
    overflow: hidden;
    color: var(--ink);
    background:
      radial-gradient(ellipse at 20% 15%, var(--mint-light) 0%, transparent 55%),
      radial-gradient(ellipse at 85% 60%, var(--mint-light) 0%, transparent 45%),
      linear-gradient(160deg, var(--mint-deep) 0%, var(--mint) 40%, var(--mint-light) 70%, var(--mint) 100%);
  }
  .author {
    position: absolute;
    top: 36px;
    left: 251px;
    font-family: "Montserrat", sans-serif;
    font-weight: 500;
    font-size: 27.5px;
    line-height: 34px;
    letter-spacing: 0.5px;
    white-space: nowrap;
  }
  .title {
    font-family: "Dancing Script", cursive;
    font-weight: 700;
    font-size: 165px;
    line-height: 1;
  }
  .title span { position: absolute; white-space: nowrap; }
  .title .line-1 { left: 50px; top: 172px; }
  .title .line-2 { left: 330px; top: 366px; }
  .title .line-3 { left: 140px; top: 584px; }
  .art { position: absolute; }
  .art-butterfly {
    left: 505px; top: 85px; width: 120px; height: 108px;
    background: radial-gradient(ellipse, var(--line-art) 0%, transparent 70%);
  }
  .art-flowers-left {
    left: 0; top: 640px; width: 215px; height: 400px;
    background: radial-gradient(ellipse at 40% 30%, var(--line-art) 0%, transparent 70%);
  }
  .art-flowers-right {
    left: 543px; top: 860px; width: 230px; height: 340px;
    background: radial-gradient(ellipse at 50% 40%, var(--line-art) 0%, transparent 70%);
  }
  .subtitle {
    position: absolute;
    top: 772px;
    left: 0;
    font-family: "Fira Sans", sans-serif;
    font-style: italic;
    font-weight: 300;
    font-size: 32px;
    line-height: 41.5px;
    letter-spacing: 0.7px;
  }
  .subtitle span { display: block; white-space: nowrap; }
  .subtitle .s1 { padding-left: 122px; }
  .subtitle .s2 { padding-left: 142px; }
  .subtitle .s3 { padding-left: 167px; }
  .subtitle .s4 { padding-left: 122px; }
  .tagline {
    position: absolute;
    top: 1008px;
    left: 118px;
    font-family: "Fira Sans", sans-serif;
    font-weight: 700;
    font-size: 25px;
    line-height: 37px;
  }
  .tagline .row { display: block; white-space: nowrap; }
  .tagline .count {
    font-style: italic;
    font-size: 40px;
    margin-right: 5px;
  }
</style>
</head>
<body>
  <main class="cover">
    <div class="author">NAME AUTOR</div>

    <div class="art art-butterfly" role="img" aria-label="Feine Linienzeichnung eines Schmetterlings"></div>

    <h1 class="title">
      <span class="line-1">Ein Garten</span>
      <span class="line-2">aus</span>
      <span class="line-3">Mondlicht</span>
    </h1>

    <div class="art art-flowers-left" role="img" aria-label="Zarte Linienzeichnung zweier Blumen an langen Stielen"></div>
    <div class="art art-flowers-right" role="img" aria-label="Zarte Linienzeichnung eines Blumenstraußes mit drei Blüten"></div>

    <p class="subtitle">
      <span class="s1">Wie du dich von negativen</span>
      <span class="s2">Gedanken befreist und</span>
      <span class="s3">eine liebevolle Beziehung</span>
      <span class="s4">zu dir selbst aufbaust</span>
    </p>

    <p class="tagline">
      <span class="row"><span class="count">12</span>lebensverändernde Monate</span>
      <span class="row">voller positiver Impulse und Liebe für dich</span>
    </p>
  </main>
</body>
</html>
```